Business Card Project for Firm Deck Hoisting

Business name is "Firm Deck Hoisting" we are a scaffolding & rigging business specialising in local and remote work for:
- scaffolding (residential, commercial, industrial)
- rigging
-man material hoists
- swing stages
- labour hire

On the back of the card I would like FDH as the symbol / logo. I have attached the logos we have had created by sketch harbour. We would like to use bold colours – preferably as the same colour scheme as the logo.

Target Market(s)

Construction business

Industry/Entity Type

Construction

Contact Information for Business Card

name: Owen Pellew
Title: Director
Phone: 0491 572 864
Address: PO BOX 3251, Marlbrook SA 5112
Email: owen@firmdeckhoisting.com.au
Website: www.firmdeckhoisting.com.au

Font styles to use
Sans Serif

Requirements
Must have
• Must use existing logo & prefering using bold colours
Nice to have
• Would be nice to have a line of dot points in what we specialise in but not essential
• Would be nice to see some designs with a slogan but not essential
Should not have
• NA

```html
<!DOCTYPE html>
<html lang="en">
<head>
<meta charset="utf-8">
<title>Firm Deck Hoisting – Business Card</title>
<link rel="stylesheet" href="https://fonts.googleapis.com/css2?family=Roboto:wght@400;500;700&display=swap">
<style>
  :root {
    --bg: #e9e7e3;
    --card-white: #fbfbfb;
    --card-grey: #e6e6e6;
    --ink: #1d1d1f;
    --ink-soft: #3a3a3c;
    --blue: #2196d3;
    --blue-deep: #1670b5;
    --blue-light: #2aa6e0;
    --black-bar: #1b1b1b;
  }
  * { box-sizing: border-box; margin: 0; padding: 0; }
  html, body {
    width: 1200px; height: 1023px; overflow: hidden;
    background: var(--bg);
    font-family: "Roboto", Arial, sans-serif;
  }
  .canvas {
    width: 1200px; height: 1023px;
    display: flex; flex-direction: column; align-items: center; justify-content: center;
    gap: 60px;
  }
  .card {
    position: relative;
    width: 700px; height: 400px;
    border-radius: 22px;
    overflow: hidden;
    box-shadow: 0 6px 18px rgba(0,0,0,0.15);
  }

  /* Front */
  .card--front {
    background: radial-gradient(ellipse at 55% 40%, var(--card-white) 0%, var(--card-grey) 100%);
    color: var(--ink);
  }
  .brand {
    position: absolute; left: 44px; top: 96px;
    display: flex; align-items: center; gap: 14px;
  }
  .brand__mark {
    width: 26px; height: 26px; background: var(--blue);
  }
  .brand__name {
    font-weight: 700; font-size: 32px; letter-spacing: 0.5px; color: var(--ink);
    text-transform: uppercase; white-space: nowrap;
  }
  .holder {
    position: absolute; right: 60px; top: 46px; text-align: right;
  }
  .holder__name {
    font-weight: 500; font-size: 28px; letter-spacing: 1px; color: var(--ink);
    white-space: nowrap;
  }
  .holder__title {
    margin-top: 4px; padding-top: 4px;
    border-top: 1px solid var(--ink-soft);
    font-size: 15px; letter-spacing: 1.5px; color: var(--blue);
  }
  .divider {
    position: absolute; left: 0; right: 290px; top: 214px;
    height: 1px; background: var(--ink-soft);
  }
  .contacts {
    position: absolute; left: 44px; bottom: 84px;
    list-style: none; font-size: 14px; letter-spacing: 1.2px; color: var(--ink-soft);
  }
  .contacts li { display: flex; align-items: center; gap: 10px; margin-top: 8px; white-space: nowrap; }
  .contacts svg { width: 14px; height: 14px; flex: none; }
  .address {
    position: absolute; right: 40px; bottom: 84px;
    font-size: 14px; letter-spacing: 1.2px; color: var(--ink-soft); white-space: nowrap;
  }
  .band {
    position: absolute; left: 0; right: 0; bottom: 34px; height: 26px;
    display: flex;
  }
  .band__blue { flex: 1; background: var(--blue); }
  .band__black { width: 60px; background: var(--black-bar); }

  /* Back */
  .card--back {
    background: radial-gradient(ellipse at 55% 45%, var(--blue-light) 0%, var(--blue) 55%, var(--blue-deep) 100%);
    display: flex; align-items: center; justify-content: center;
  }
  .card--back .brand { position: static; }
  .card--back .brand__mark { width: 34px; height: 34px; background: #ffffff; }
  .card--back .brand__name { color: #ffffff; font-size: 46px; }
</style>
</head>
<body>
<main class="canvas">
  <section class="card card--front" aria-label="Card front">
    <div class="brand">
      <span class="brand__mark"></span>
      <span class="brand__name">Firm Deck Hoisting</span>
    </div>
    <div class="holder">
      <p class="holder__name">Owen Pellew</p>
      <p class="holder__title">Director</p>
    </div>
    <div class="divider"></div>
    <ul class="contacts">
      <li>
        <svg viewBox="0 0 16 16" aria-hidden="true"><circle cx="8" cy="8" r="7" fill="none" stroke="#2196d3" stroke-width="1.4"/><path d="M5.5 4.5l1.5 1.6-0.8 1c0.6 1.2 1.4 2 2.6 2.6l1-0.8 1.6 1.5-1 1.2c-2.8-0.6-5-2.8-5.6-5.6z" fill="#2196d3"/></svg>
        0491 572 864
      </li>
      <li>
        <svg viewBox="0 0 16 16" aria-hidden="true"><rect x="1.5" y="3.5" width="13" height="9" fill="none" stroke="#2196d3" stroke-width="1.4"/><path d="M1.5 3.5l6.5 5 6.5-5" fill="none" stroke="#2196d3" stroke-width="1.4"/></svg>
        owen@firmdeckhoisting.com.au
      </li>
      <li>
        <svg viewBox="0 0 16 16" aria-hidden="true"><circle cx="8" cy="8" r="6.5" fill="none" stroke="#2196d3" stroke-width="1.4"/><ellipse cx="8" cy="8" rx="3" ry="6.5" fill="none" stroke="#2196d3" stroke-width="1.2"/><path d="M1.5 8h13" stroke="#2196d3" stroke-width="1.2"/></svg>
        www.firmdeckhoisting.com.au
      </li>
    </ul>
    <p class="address">PO BOX 3251, Marlbrook SA 5112</p>
    <div class="band"><span class="band__blue"></span><span class="band__black"></span></div>
  </section>

  <section class="card card--back" aria-label="Card back">
    <div class="brand">
      <span class="brand__mark"></span>
      <span class="brand__name">Firm Deck Hoisting</span>
    </div>
  </section>
</main>
</body>
</html>
```